brindle cafe flyer design project

A funky trendy cafe in Melbourne’s CBD that caters too a large range of corporate clients. Located on the door step of a major train station, its a quick turn around cafe for the short time frame customer but also a cafe to sit, relax and enjoy the hustle and bustle from the inside out. We provide All day breakfast, gourmet sandwiches, gourmet rotti wraps, a la carte menu and also heat and serve meals.

BREAKFAST TO GO! ALL BREAKFAST TO GO ITEMS COME WITH A MEDIUM TAKE AWAY COFFEE!
• RAISIN TOAST & COFFEE – $6
• BACON & EGG MUFFIN & COFFEE $7.5
• SPINACH, MUSHROOM OMELETTE MUFFIN & COFFEE $7.5
• OMELETTE WITH CHEESE MUFFIN & COFFEE $7.5
• HAM & CHEESE CROISSANT & COFFEE $7.5
• SWEET OR SAVOURY MUFFIN & COFFEE $6.5
• HAM & CHEESE SANDWICH & COFFEE $8.0
• HAM, CHEESE & TOMATO SANDWICH & COFFEE $8.5

*NOT IN CONJUNCTION WITH BRINDLE CLUB CARD OFFER

WE ALSO HAVE PRE-MADE LUNCH OPTIONS – ASSORTED ROTTI WRAPS (Bbq chicken, honey mustard chicken, pesto chicken & vegetarian) ASSORTED GOURMET SANDWICHES (Mediterranean, Moroccan chicken, Salami, Chicken Schnitzel, Salmon, Brindle & Roast Beef) Soup of the day Pasta of the day Salad of the day

Ph- 03 9517 8836 Fax- 03 9517 8839 Web – www.brindlecafe.com.au 418 KESTREL LANE MELBOURNE 3000

Industry/Entity Type

Cafe

Font styles to use
Serif

Requirements
Must have
• Our 2 branded colours -

PMS 392c
PMS BLACK

```html
<!DOCTYPE html>
<html lang="en">
<head>
<meta charset="utf-8">
<title>Brindle Cafe – Breakfast To Go Flyer</title>
<link href="https://fonts.googleapis.com/css2?family=Open+Sans:wght@400;600;700&family=Raleway:wght@100;200&display=swap" rel="stylesheet">
<style>
  :root {
    --brand-green: #a6e000;
    --brand-green-light: #cdf25c;
    --brand-green-pale: #e4f9a0;
    --brand-black: #000000;
    --ink-grey: #4a4a4a;
    --fine-grey: #262626;
    --paper: #ffffff;
  }
  html, body {
    margin: 0;
    padding: 0;
    width: 1200px;
    height: 2544px;
    overflow: hidden;
    background: var(--paper);
  }
  .flyer {
    position: relative;
    width: 1200px;
    height: 2544px;
    overflow: hidden;
    background: var(--paper);
    font-family: "Open Sans", Arial, sans-serif;
  }
  .menu-panel {
    position: absolute;
    left: 0;
    top: 1380px;
    width: 1200px;
    height: 1164px;
    background: var(--brand-black);
  }
  .brand-mark {
    position: absolute;
    left: 78px;
    top: 68px;
    width: 376px;
    height: 373px;
    background: var(--brand-black);
    display: flex;
    flex-direction: column;
    align-items: center;
    justify-content: center;
    gap: 34px;
    z-index: 2;
  }
  .brand-mark__dot {
    width: 120px;
    height: 120px;
    border-radius: 50%;
    background: var(--brand-green);
  }
  .brand-mark__name {
    color: var(--brand-green);
    font-weight: 400;
    font-size: 44px;
    letter-spacing: 4px;
  }
  .contact {
    position: absolute;
    left: 619px;
    top: 64px;
    margin: 0;
    padding: 0;
    list-style: none;
    color: var(--ink-grey);
    font-size: 45px;
    line-height: 86px;
    z-index: 2;
  }
  .waves {
    position: absolute;
    left: 0;
    top: 0;
    width: 1200px;
    height: 1500px;
  }
  .tagline {
    position: absolute;
    left: 92px;
    top: 700px;
    margin: 0;
    font-family: "Raleway", "Open Sans", sans-serif;
    font-weight: 200;
    font-size: 122px;
    line-height: 122px;
    color: #111;
  }
  .tagline span { display: block; }
  .menu {
    position: absolute;
    left: 163px;
    top: 1452px;
    width: 900px;
    margin: 0;
    padding: 0;
    list-style: none;
    color: var(--paper);
  }
  .menu__item {
    display: flex;
    justify-content: space-between;
    align-items: flex-start;
    margin-bottom: 22px;
  }
  .menu__name {
    width: 710px;
    font-size: 34px;
    line-height: 52px;
    letter-spacing: 0.5px;
    text-align: justify;
  }
  .menu__name--wide { letter-spacing: 5px; }
  .menu__price {
    width: 140px;
    color: var(--brand-green);
    font-weight: 700;
    font-size: 41px;
    line-height: 52px;
  }
  .lunch {
    position: absolute;
    left: 163px;
    top: 2112px;
    width: 880px;
    color: var(--fine-grey);
  }
  .lunch__title {
    margin: 0 0 4px;
    font-size: 28px;
    font-weight: 700;
    color: #3a3a3a;
  }
  .lunch__list {
    margin: 0;
    font-size: 19px;
    line-height: 28px;
    text-align: justify;
  }
  .website {
    position: absolute;
    left: 0;
    top: 2408px;
    width: 1200px;
    text-align: center;
    color: var(--brand-green);
    font-weight: 600;
    font-size: 48px;
    letter-spacing: 19px;
  }
</style>
</head>
<body>
<main class="flyer">

  <div class="menu-panel"></div>

  <svg class="waves" viewBox="0 0 1200 1500">
    <defs>
      <linearGradient id="photoTone" x1="0" y1="0" x2="1" y2="0.3">
        <stop offset="0" stop-color="#6e4a36"/>
        <stop offset="0.35" stop-color="#b58c74"/>
        <stop offset="0.7" stop-color="#d9b8a2"/>
        <stop offset="1" stop-color="#7a5240"/>
      </linearGradient>
    </defs>
    <path d="M0 470 C400 470 820 440 1200 390 L1200 520 C800 540 400 560 0 600 Z" fill="var(--brand-green-light)"/>
    <path d="M0 480 C420 500 820 470 1200 420 L1200 470 C800 500 400 520 0 530 Z" fill="var(--brand-green)"/>
    <g role="img" aria-label="Photograph of a woman in profile sipping from a white coffee cup in a warm cafe setting">
      <path d="M0 560 C400 545 800 515 1200 480 L1200 1160 C800 1200 400 1250 0 1260 Z" fill="url(#photoTone)"/>
    </g>
    <path d="M0 1120 C400 1190 800 1160 1200 1110 L1200 1300 L0 1400 Z" fill="var(--brand-green-pale)"/>
    <path d="M0 1210 C400 1235 800 1200 1200 1165 L1200 1300 L0 1400 Z" fill="var(--brand-green-light)"/>
    <path d="M0 1385 C400 1340 800 1300 1200 1285 L1200 1500 L0 1500 Z" fill="var(--brand-black)"/>
  </svg>

  <div class="brand-mark">
    <span class="brand-mark__dot"></span>
    <span class="brand-mark__name">BRINDLE</span>
  </div>

  <ul class="contact">
    <li>Ph: 03 9517 8836</li>
    <li>Fax: 03 9517 8839</li>
    <li>418 Kestrel Lane</li>
    <li>Melbourne 3000</li>
  </ul>

  <h1 class="tagline">
    <span>eat...</span>
    <span>treat...</span>
    <span>repeat...</span>
  </h1>

  <ul class="menu">
    <li class="menu__item"><span class="menu__name">RAISIN TOAST &amp; COFFEE</span><span class="menu__price">$6</span></li>
    <li class="menu__item"><span class="menu__name">BACON &amp; EGG MUFFIN &amp; COFFEE</span><span class="menu__price">$7.5</span></li>
    <li class="menu__item"><span class="menu__name menu__name--wide">SPINACH, MUSHROOM OMELETTE MUFFIN &amp; COFFEE</span><span class="menu__price">$7.5</span></li>
    <li class="menu__item"><span class="menu__name">OMELETTE MUFFIN &amp; COFFEE</span><span class="menu__price">$7.5</span></li>
    <li class="menu__item"><span class="menu__name menu__name--wide">OMELETTE WITH CHEESE MUFFIN &amp; COFFEE</span><span class="menu__price">$7.5</span></li>
    <li class="menu__item"><span class="menu__name">HAM &amp; CHEESE CROISSANT &amp; COFFEE</span><span class="menu__price">$6.5</span></li>
    <li class="menu__item"><span class="menu__name">SWEET OR SAVOURY MUFFIN &amp; COFFEE</span><span class="menu__price">$8.0</span></li>
    <li class="menu__item"><span class="menu__name">HAM &amp; CHEESE SANDWICH &amp; COFFEE</span><span class="menu__price">$8.5</span></li>
  </ul>

  <section class="lunch">
    <h2 class="lunch__title">PRE-MADE LUNCH OPTIONS</h2>
    <p class="lunch__list">ASSORTED ROTTI WRAPS (Bbq chicken, honey mustard chicken, pesto chicken &amp; vegetarian) ASSORTED GOURMET SANDWICHES (Mediterranean, Moroccan chicken, Salami, Chicken Schnitzel, Salmon, Brindle &amp; Roast Beef) Soup of the day Pasta of the day Salad of the day.</p>
  </section>

  <div class="website">www.brindlecafe.com.au</div>

</main>
</body>
</html>
```